Welbourne Dental, P.C. New stationary and business card for modern Dental Office

We need a new stationary/envelope/business card design using our newly designed logo. We are looking for an upscale look. Our new logo is used on our signage, using black as the background and white for the lettering. We would like the stationary to have black, white, possible greys or silver. We are looking for a letterhead, envelope, and business card design for three different employees, as well as a 4th card, same design, but just general with no employee name.

Project Deadline Extended
Reason: We began this project in the middle of our move into our new office. Things got pretty hectic and we just didn't have the time to go through designs. We now settled in and finally eliminated the designs that didn't work for us. We would like to extend the project another 5 days, and then finalize our decision. Most of the submissions showed business cards alone, with no stationary designs. Our original request was for stationary and business cards. Please keep this in mind.

Target Market(s)

Dental patients expecting high quality, cosmetic dentistry

Industry/Entity Type

Business

Contact Information for Business Card

Will need a design using our logo. All cards will be the same, other than that one card will have Office Managers name, One for the Doctor, Hygienist,
1. Office Manager - Marisol Dubrovka
2. Hygienist - Kayleigh Morrow
3. Gordon T. Welbourne, D.D.S.
4. One general one with no staff names

Font styles to use
Other font styles liked:
• see upload

Colors
000000
1b1b1b
757575
c9c9c9
e8e8e8
ffffff

Requirements
Must have
• -Logo
• -Phone number (718)555-0193
• -Address: 4352 63rd Ave
• Lower Level
• Brooklyn, NY 11290

```html
<!DOCTYPE html>
<html lang="en">
<head>
<meta charset="utf-8">
<title>Welbourne Dental, P.C. — Stationery Set</title>
<link rel="stylesheet" href="https://fonts.googleapis.com/css2?family=Open+Sans:wght@400;600;700&display=swap">
<style>
  :root {
    --black: #000000;
    --ink: #1b1b1b;
    --mid-grey: #757575;
    --silver: #c9c9c9;
    --pale: #e8e8e8;
    --white: #ffffff;
    --backdrop: #efefef;
  }
  * { box-sizing: border-box; margin: 0; padding: 0; }
  html, body { width: 945px; height: 1200px; overflow: hidden; }
  body {
    background: var(--backdrop);
    font-family: "Open Sans", Arial, sans-serif;
    color: var(--ink);
    position: relative;
  }
  .sheet { position: absolute; overflow: hidden; box-shadow: 0 2px 10px rgba(0,0,0,.12); }
  .sheet > svg.shapes { position: absolute; inset: 0; }

  /* Logo: name in text font with one plain circle */
  .logo { position: absolute; display: flex; align-items: center; white-space: nowrap; }
  .logo-name { font-weight: 700; color: var(--black); line-height: 1; }
  .logo-ring { display: inline-block; width: 1em; height: 1em; border: 2px solid var(--black); border-radius: 50%; margin-left: .35em; }
  .logo.small .logo-ring { border-width: 1px; }

  /* Small business cards (general, no staff name) */
  .mini { left: 20px; width: 170px; height: 97px; }
  .mini-front { top: 190px; background: var(--silver); }
  .mini-front .logo { left: 50%; top: 50%; transform: translate(-50%, -50%); font-size: 8px; }
  .mini-back { top: 305px; background: var(--white); }
  .mini-back .logo { left: 12px; top: 14px; font-size: 8px; }
  .mini-back .contact { position: absolute; left: 12px; top: 32px; font-size: 5.5px; line-height: 1.5; }
  .mini-back .tel { position: absolute; left: 104px; top: 76px; font-size: 5.5px; }

  /* Letterhead */
  .letterhead { left: 210px; top: 24px; width: 350px; height: 495px; background: var(--white); }
  .letterhead .logo { left: 94px; top: 22px; font-size: 13px; }
  .letterhead .sender { position: absolute; left: 56px; top: 46px; font-size: 6px; line-height: 1.55; }
  .letterhead .body { position: absolute; left: 56px; top: 108px; width: 250px; font-size: 7px; line-height: 1.7; }
  .letterhead .body p { margin-bottom: 8px; text-align: justify; }

  /* Presentation folder */
  .folder { left: 580px; top: 24px; width: 345px; height: 495px; background: var(--silver); }
  .folder .logo { left: 50%; top: 50%; transform: translate(-50%, -50%); font-size: 20px; }

  /* Envelope */
  .envelope { left: 210px; top: 545px; width: 520px; height: 226px; background: var(--white); }
  .envelope .logo { left: 58px; top: 16px; font-size: 13px; }
  .envelope .return-address { position: absolute; left: 58px; top: 36px; font-size: 6px; line-height: 1.55; }

  /* Staff business cards */
  .card { top: 805px; width: 425px; height: 245px; }
  .card-front { left: 30px; background: var(--silver); }
  .card-front .logo { left: 50%; top: 50%; transform: translate(-50%, -50%); font-size: 21px; }
  .card-back { left: 490px; background: var(--white); }
  .card-back .logo { left: 22px; top: 92px; font-size: 15px; }
  .card-back .contact { position: absolute; left: 262px; top: 36px; font-size: 10px; line-height: 1.45; }
  .contact .person { font-weight: 700; }
  .contact .role { margin-bottom: 12px; }
  .contact .label { font-weight: 700; }
</style>
</head>
<body>

  <!-- General business card, front -->
  <section class="sheet mini mini-front" aria-label="General business card front">
    <div class="logo small"><span class="logo-name">Welbourne Dental, P.C.</span><span class="logo-ring"></span></div>
  </section>

  <!-- General business card, back -->
  <section class="sheet mini mini-back" aria-label="General business card back">
    <svg class="shapes" width="170" height="97" viewBox="0 0 170 97" aria-hidden="true">
      <polygon points="0,86 92,86 86,94 0,94" fill="var(--black)"/>
      <polygon points="98,82 170,82 170,94 90,94" fill="var(--silver)"/>
    </svg>
    <div class="logo small"><span class="logo-name">Welbourne Dental, P.C.</span><span class="logo-ring"></span></div>
    <div class="contact">
      <span class="label">Address:</span><br>
      4352 63rd Ave Lower Level<br>
      Brooklyn, NY 11290
    </div>
    <div class="tel"><b>Tel :</b> (718)555-0193</div>
  </section>

  <!-- Letterhead -->
  <section class="sheet letterhead" aria-label="Letterhead">
    <svg class="shapes" width="350" height="495" viewBox="0 0 350 495" aria-hidden="true">
      <rect x="56" y="21" width="33" height="7" fill="var(--black)"/>
      <rect x="184" y="68" width="166" height="8" fill="var(--silver)"/>
      <polygon points="0,468 187,468 171,486 0,486" fill="var(--black)"/>
      <polygon points="194,476 350,476 350,486 185,486" fill="var(--silver)"/>
    </svg>
    <div class="logo"><span class="logo-name">Welbourne Dental, P.C.</span><span class="logo-ring"></span></div>
    <div class="sender">
      Gordon T. Welbourne, D.D.S.<br>
      Address:<br>
      4352 63rd Ave Lower Level<br>
      Brooklyn, NY 11290<br>
      Tel: (718)555-0193
    </div>
    <div class="body">
      <p>Thank you for choosing our practice for your dental care. We look forward to welcoming you to our new office and providing a comfortable, modern visit for the whole family.</p>
      <p>Our team offers general and cosmetic treatment, from routine cleanings and fillings to whitening and veneers. Every plan is shaped around your goals and explained clearly before we begin.</p>
      <p>Please arrive ten minutes early for your first appointment and bring your insurance card. If you have any questions, call our front desk and we will gladly help.</p>
      <p>Warm regards,</p>
    </div>
  </section>

  <!-- Presentation folder -->
  <section class="sheet folder" aria-label="Presentation folder">
    <div class="logo"><span class="logo-name">Welbourne Dental, P.C.</span><span class="logo-ring"></span></div>
  </section>

  <!-- Envelope -->
  <section class="sheet envelope" aria-label="Envelope">
    <svg class="shapes" width="520" height="226" viewBox="0 0 520 226" aria-hidden="true">
      <rect x="22" y="15" width="30" height="7" fill="var(--black)"/>
      <rect x="224" y="56" width="296" height="9" fill="var(--silver)"/>
      <polygon points="0,184 230,184 210,212 0,212" fill="var(--black)"/>
      <polygon points="238,194 520,194 520,212 226,212" fill="var(--silver)"/>
    </svg>
    <div class="logo"><span class="logo-name">Welbourne Dental, P.C.</span><span class="logo-ring"></span></div>
    <div class="return-address">
      4352 63rd Ave Lower Level<br>
      Brooklyn, NY 11290
    </div>
  </section>

  <!-- Staff business card, front -->
  <section class="sheet card card-front" aria-label="Business card front">
    <div class="logo"><span class="logo-name">Welbourne Dental, P.C.</span><span class="logo-ring"></span></div>
  </section>

  <!-- Staff business card, back -->
  <section class="sheet card card-back" aria-label="Business card back">
    <svg class="shapes" width="425" height="245" viewBox="0 0 425 245" aria-hidden="true">
      <polygon points="0,208 304,208 288,230 0,230" fill="var(--black)"/>
      <polygon points="322,180 425,180 425,230 296,230" fill="var(--silver)"/>
    </svg>
    <div class="logo"><span class="logo-name">Welbourne Dental, P.C.</span><span class="logo-ring"></span></div>
    <div class="contact">
      <div class="person">Gordon T. Welbourne, D.D.S.</div>
      <div class="role">Dentist</div>
      <div class="label">Address :</div>
      <div>4352 63rd Ave Lower Level,</div>
      <div>Brooklyn, NY 11290</div>
      <div><span class="label">Tel :</span> (718)555-0193</div>
    </div>
  </section>

</body>
</html>
```